Poly Bag Packaging Motorcycle Cables - Vorenza Brand

Poly Bag Dimensions: 33cm(H) x 24cm(W)
We would like to design a genuine Poly Bag Packaging for motorcycle cables.
Vorenza, is one of the leading companies for manufacturing Motorcycles, located in Egypt. Our company is offering high-quality products, the best in the local market, with very competitive prices.
We have a limited time to get this project done, So we Highly appreciate receiving your designs ASAP.
Target Market(s)
Motorcycle Spare parts Buyers
Colors
Designer to choose colors to be used in the design.
Look and feel

```html
<!DOCTYPE html>
<html lang="en">
<head>
<meta charset="utf-8">
<title>Vorenza Motorcycle Cables – Poly Bag</title>
<link rel="stylesheet" href="https://fonts.googleapis.com/css2?family=Bebas+Neue&family=Open+Sans:wght@400&display=swap">
<style>
  :root {
    --sheet: #ffffff;
    --ink: #231f20;
    --yellow: #ffed00;
    --blue: #0088ce;
    --red: #e33b25;
    --edge: #c8c8c8;
    --note: #2b2b2b;
  }
  * { box-sizing: border-box; margin: 0; padding: 0; }
  html, body { width: 1200px; height: 980px; overflow: hidden; background: var(--sheet); }
  .sheet { position: relative; width: 1200px; height: 980px; border: 1px solid #e2e2e2; }
  .print-note {
    position: absolute; left: 203px; top: 118px;
    font-family: "Open Sans", Arial, sans-serif; font-size: 25px; color: var(--note);
  }
  .bag {
    position: absolute; top: 196px; width: 414px; height: 569px;
    border: 1px solid var(--edge); background: var(--sheet);
  }
  .bag--blue { left: 161px; }
  .bag--red { left: 623px; }
  .bag svg { display: block; width: 100%; height: 100%; }
  .headline { font-family: "Bebas Neue", "Oswald", sans-serif; fill: var(--ink); }
  .brand-name { font-family: "Bebas Neue", "Oswald", sans-serif; fill: #ffffff; }
  .mini-name { font-family: "Bebas Neue", "Oswald", sans-serif; fill: var(--ink); }
</style>
</head>
<body>
<svg width="0" height="0" style="position:absolute" aria-hidden="true">
  <defs>
    <symbol id="mini-mark" viewBox="0 0 44 44">
      <circle cx="22" cy="16" r="12" fill="#fff" stroke="#231f20" stroke-width="3"/>
      <text class="mini-name" x="22" y="40" text-anchor="middle" font-size="10" letter-spacing="0.5">VORENZA</text>
    </symbol>
  </defs>
</svg>

<main class="sheet">
  <p class="print-note">3 clour printing &nbsp;- white is transparent</p>

  <section class="bag bag--blue" aria-label="Blue poly bag version">
    <svg viewBox="0 0 734 1009" preserveAspectRatio="none">
      <g class="pattern-top">
        <use href="#mini-mark" x="102" y="39" width="44" height="44"/>
        <use href="#mini-mark" x="202" y="39" width="44" height="44"/>
        <use href="#mini-mark" x="302" y="39" width="44" height="44"/>
        <use href="#mini-mark" x="402" y="39" width="44" height="44"/>
        <use href="#mini-mark" x="501" y="39" width="44" height="44"/>
        <use href="#mini-mark" x="601" y="39" width="44" height="44"/>
        <use href="#mini-mark" x="47" y="111" width="44" height="44"/>
        <use href="#mini-mark" x="147" y="111" width="44" height="44"/>
        <use href="#mini-mark" x="247" y="111" width="44" height="44"/>
        <use href="#mini-mark" x="347" y="111" width="44" height="44"/>
        <use href="#mini-mark" x="446" y="111" width="44" height="44"/>
        <use href="#mini-mark" x="546" y="111" width="44" height="44"/>
        <use href="#mini-mark" x="105" y="186" width="44" height="44"/>
        <use href="#mini-mark" x="205" y="186" width="44" height="44"/>
        <use href="#mini-mark" x="305" y="186" width="44" height="44"/>
        <use href="#mini-mark" x="405" y="186" width="44" height="44"/>
        <use href="#mini-mark" x="504" y="186" width="44" height="44"/>
        <use href="#mini-mark" x="604" y="186" width="44" height="44"/>
      </g>
      <polygon class="color-band" fill="var(--blue)" points="0,388 734,246 734,704 0,846"/>
      <polygon fill="var(--yellow)" points="0,325 311,268 311,328 0,388"/>
      <polygon fill="#fff" points="0,410 216,367 216,377 0,420"/>
      <text class="headline" x="183" y="338" text-anchor="middle" font-size="52" transform="rotate(-11 183 325)">HIGH QUALITY</text>
      <circle cx="609" cy="378" r="67" fill="#fff"/>
      <circle cx="609" cy="378" r="60" fill="var(--yellow)"/>
      <circle cx="367" cy="490" r="125" fill="var(--ink)"/>
      <text class="brand-name" x="367" y="685" text-anchor="middle" font-size="74" letter-spacing="3">VORENZA</text>
      <g class="pattern-bottom">
        <use href="#mini-mark" x="89" y="756" width="44" height="44"/>
        <use href="#mini-mark" x="195" y="756" width="44" height="44"/>
        <use href="#mini-mark" x="29" y="834" width="44" height="44"/>
        <use href="#mini-mark" x="135" y="834" width="44" height="44"/>
        <use href="#mini-mark" x="347" y="834" width="44" height="44"/>
        <use href="#mini-mark" x="454" y="834" width="44" height="44"/>
        <use href="#mini-mark" x="560" y="834" width="44" height="44"/>
        <use href="#mini-mark" x="91" y="914" width="44" height="44"/>
        <use href="#mini-mark" x="197" y="914" width="44" height="44"/>
        <use href="#mini-mark" x="303" y="914" width="44" height="44"/>
        <use href="#mini-mark" x="409" y="914" width="44" height="44"/>
        <use href="#mini-mark" x="515" y="914" width="44" height="44"/>
        <use href="#mini-mark" x="621" y="914" width="44" height="44"/>
      </g>
      <polygon fill="var(--yellow)" points="245,775 734,681 734,779 245,873"/>
      <text class="headline" x="489" y="795" text-anchor="middle" font-size="72" transform="rotate(-11 489 773)">MOTOR CYCLE CABLES</text>
    </svg>
  </section>

  <section class="bag bag--red" aria-label="Red poly bag version">
    <svg viewBox="0 0 734 1009" preserveAspectRatio="none">
      <g class="pattern-top">
        <use href="#mini-mark" x="102" y="39" width="44" height="44"/>
        <use href="#mini-mark" x="202" y="39" width="44" height="44"/>
        <use href="#mini-mark" x="302" y="39" width="44" height="44"/>
        <use href="#mini-mark" x="402" y="39" width="44" height="44"/>
        <use href="#mini-mark" x="501" y="39" width="44" height="44"/>
        <use href="#mini-mark" x="601" y="39" width="44" height="44"/>
        <use href="#mini-mark" x="47" y="111" width="44" height="44"/>
        <use href="#mini-mark" x="147" y="111" width="44" height="44"/>
        <use href="#mini-mark" x="247" y="111" width="44" height="44"/>
        <use href="#mini-mark" x="347" y="111" width="44" height="44"/>
        <use href="#mini-mark" x="446" y="111" width="44" height="44"/>
        <use href="#mini-mark" x="546" y="111" width="44" height="44"/>
        <use href="#mini-mark" x="105" y="186" width="44" height="44"/>
        <use href="#mini-mark" x="205" y="186" width="44" height="44"/>
        <use href="#mini-mark" x="305" y="186" width="44" height="44"/>
        <use href="#mini-mark" x="405" y="186" width="44" height="44"/>
        <use href="#mini-mark" x="504" y="186" width="44" height="44"/>
        <use href="#mini-mark" x="604" y="186" width="44" height="44"/>
      </g>
      <polygon class="color-band" fill="var(--red)" points="0,388 734,246 734,704 0,846"/>
      <polygon fill="var(--yellow)" points="0,325 311,268 311,328 0,388"/>
      <polygon fill="#fff" points="0,410 205,369 205,379 0,420"/>
      <text class="headline" x="183" y="338" text-anchor="middle" font-size="52" transform="rotate(-11 183 325)">HIGH QUALITY</text>
      <circle cx="617" cy="378" r="67" fill="#fff"/>
      <circle cx="617" cy="378" r="60" fill="var(--yellow)"/>
      <circle cx="377" cy="490" r="125" fill="var(--ink)"/>
      <text class="brand-name" x="377" y="683" text-anchor="middle" font-size="74" letter-spacing="3">VORENZA</text>
      <g class="pattern-bottom">
        <use href="#mini-mark" x="89" y="756" width="44" height="44"/>
        <use href="#mini-mark" x="195" y="756" width="44" height="44"/>
        <use href="#mini-mark" x="30" y="834" width="44" height="44"/>
        <use href="#mini-mark" x="136" y="834" width="44" height="44"/>
        <use href="#mini-mark" x="348" y="834" width="44" height="44"/>
        <use href="#mini-mark" x="454" y="834" width="44" height="44"/>
        <use href="#mini-mark" x="560" y="834" width="44" height="44"/>
        <use href="#mini-mark" x="91" y="914" width="44" height="44"/>
        <use href="#mini-mark" x="197" y="914" width="44" height="44"/>
        <use href="#mini-mark" x="303" y="914" width="44" height="44"/>
        <use href="#mini-mark" x="409" y="914" width="44" height="44"/>
        <use href="#mini-mark" x="515" y="914" width="44" height="44"/>
        <use href="#mini-mark" x="621" y="914" width="44" height="44"/>
      </g>
      <polygon fill="var(--yellow)" points="246,762 734,668 734,766 246,860"/>
      <polygon fill="var(--ink)" points="550,818 734,783 734,794 550,829"/>
      <text class="headline" x="490" y="782" text-anchor="middle" font-size="72" transform="rotate(-11 490 760)">MOTOR CYCLE CABLES</text>
    </svg>
  </section>
</main>
</body>
</html>
```